Adventurous female pilot

I am looking for a personal business card, for a very well qualified female pilot, with a lot of aviation experience.

Currently an airline pilot, have worked as a bush pilot in Africa, looking to get into corporate aviation, or private jet owners.
Want a classy looking card for networking...

Could be interested in a retro\vintage look also?!

An idea,, is an african sunset background, with my wings\logo on it
Updates

I just want to say thank you to all of your for your amazing designs!

I have been very busy flying this past week , so not had a chance to be on the computer much.
But I provide some feedback, and conclusions very soon!
Thank you again.

Marla

Reason: Still waiting on a couple of revisions to be 100% about my choice!

Target Market(s)

corporate aviation, private jet owners, casino's,
General audience.
networking

Industry/Entity Type

Airline

Requirements
Nice to have
• Classy, edgy, sexy, but also feminine

```html
<!DOCTYPE html>
<html lang="en">
<head>
<meta charset="utf-8">
<title>Marla Hollis Business Card</title>
<link rel="stylesheet" href="https://fonts.googleapis.com/css2?family=Ubuntu:wght@400;500&display=swap">
<style>
  :root {
    --page-bg: #2b2d31;
    --card-navy: #1b2029;
    --sky-top: #2f8fe0;
    --sky-mid: #4a7fd6;
    --sky-deep: #1e3f9a;
    --band-blue: #3aa3db;
    --band-blue-dark: #1f86c4;
    --band-white: #ffffff;
    --text-light: #f2f4f7;
    --flag-red: #c8262d;
    --flag-blue: #2a3d8f;
  }
  * { margin: 0; padding: 0; box-sizing: border-box; }
  html, body {
    width: 1200px; height: 861px; overflow: hidden;
    background: var(--page-bg);
  }
  .card {
    position: absolute; left: 150px; top: 173px;
    width: 900px; height: 514px;
    background: var(--card-navy);
    border-radius: 6px;
    overflow: hidden;
    box-shadow: 0 20px 50px rgba(0,0,0,0.45);
    font-family: "Ubuntu", sans-serif;
    color: var(--text-light);
  }
  .card-art { position: absolute; inset: 0; width: 900px; height: 514px; }
  .holder-name {
    position: absolute; left: 40px; top: 365px;
    font-size: 44px; font-weight: 500; letter-spacing: 0.5px;
  }
  .contact-list {
    position: absolute; left: 455px; top: 322px;
    list-style: none;
  }
  .contact-item {
    display: flex; align-items: center; gap: 12px;
    height: 46px; font-size: 24px; font-weight: 400;
  }
  .contact-icon {
    width: 32px; height: 32px; border-radius: 50%;
    border: 2px solid var(--text-light);
    display: flex; align-items: center; justify-content: center;
    flex-shrink: 0;
  }
  .flag {
    width: 30px; height: 20px; flex-shrink: 0;
    display: block;
  }
  .region { font-weight: 500; }
</style>
</head>
<body>
  <section class="card">
    <svg class="card-art" viewBox="0 0 900 514" xmlns="http://www.w3.org/2000/svg">
      <defs>
        <linearGradient id="band-gradient" x1="0" y1="0" x2="1" y2="0">
          <stop offset="0" stop-color="var(--band-blue)"/>
          <stop offset="1" stop-color="var(--band-blue-dark)"/>
        </linearGradient>
        <linearGradient id="sky-gradient" x1="0" y1="0" x2="0" y2="1">
          <stop offset="0" stop-color="var(--sky-top)"/>
          <stop offset="0.5" stop-color="var(--sky-mid)"/>
          <stop offset="1" stop-color="var(--sky-deep)"/>
        </linearGradient>
      </defs>
      <path class="accent-band" fill="url(#band-gradient)"
        d="M0,0 H900 V120 L395,300 Q330,322 265,298 L0,190 Z"/>
      <path class="white-band" fill="var(--band-white)"
        d="M0,0 H900 V98 L385,270 Q330,290 275,270 L0,162 Z"/>
      <g role="img" aria-label="Illustration of a jet airliner wing with two engines flying above the clouds in a blue sky">
        <path class="sky-illustration" fill="url(#sky-gradient)"
          d="M0,0 H900 V84 L380,254 Q330,272 280,254 L0,148 Z"/>
      </g>
    </svg>

    <h1 class="holder-name">MARLA HOLLIS</h1>

    <ul class="contact-list">
      <li class="contact-item">
        <span class="contact-icon">
          <svg width="16" height="12" viewBox="0 0 16 12"><rect x="0.5" y="0.5" width="15" height="11" fill="var(--text-light)"/><path d="M0.5,0.5 L8,7 L15.5,0.5" fill="none" stroke="var(--card-navy)" stroke-width="1.4"/></svg>
        </span>
        <span>marlachollis@skymail.net</span>
      </li>
      <li class="contact-item">
        <span class="contact-icon">
          <svg width="12" height="18" viewBox="0 0 12 18"><rect x="1" y="1" width="10" height="16" rx="2" fill="none" stroke="var(--text-light)" stroke-width="1.6"/><rect x="3" y="3.5" width="6" height="5" fill="var(--text-light)"/></svg>
        </span>
        <svg class="flag" viewBox="0 0 30 20" aria-hidden="true"><rect width="30" height="20" fill="var(--flag-red)"/><rect y="4" width="30" height="3" fill="#fff"/><rect y="10" width="30" height="3" fill="#fff"/><rect y="16" width="30" height="2" fill="#fff"/><rect width="13" height="10" fill="var(--flag-blue)"/></svg>
        <span><span class="region">US</span> +1 702-555-0148</span>
      </li>
      <li class="contact-item">
        <span class="contact-icon">
          <svg width="12" height="18" viewBox="0 0 12 18"><rect x="1" y="1" width="10" height="16" rx="2" fill="none" stroke="var(--text-light)" stroke-width="1.6"/><rect x="3" y="3.5" width="6" height="5" fill="var(--text-light)"/></svg>
        </span>
        <svg class="flag" viewBox="0 0 30 20" aria-hidden="true"><rect width="30" height="20" fill="var(--flag-red)"/><rect width="15" height="10" fill="var(--flag-blue)"/><circle cx="7.5" cy="5" r="2.5" fill="#fff"/></svg>
        <span><span class="region">Taipei</span> +886 970-555-214</span>
      </li>
    </ul>
  </section>
</body>
</html>
```